Wordpress Design Project

Good day.

I was hoping to buy a professional looking Wordpress template and just fill in the blanks with my personal data and start blogging, but unfortunately my blog posts need to include images that are 756 pixels x 439.

A sample image can be found at.
http://files.brindlecache.net/7-Pics/layoutsample.gif

So, I need your help.

1 This is a daily newsletter / blog site only. Not a corporate site.
2 Subject - Stock Market
2 I have no color preferences. I will leave that up to you.
I would like something that looks like this
http://preview.loftmerath.com/clarity/
3 I would like to include Vortelli Ads on both the Home Page and within each post.
4 The home page should show a link and a short summary to each post.
5 The home page should include an email capture box. We use MailChimp)
6 The home page should include a Site Search Box and function.
7 The home page should include a External Links Box.

If I have forgotten anything, please let me know.
I welcome your suggestions.

I look forward to seeing your designs and picking a winner.

Thank you for reading my post.

Darren Oakhurst

Vortelli

```html
<!DOCTYPE html>
<html lang="en">
<head>
<meta charset="utf-8">
<title>Stock Market — Post</title>
<link href="https://fonts.googleapis.com/css2?family=Cabin:ital,wght@0,400;0,600;0,700;1,400&family=Noto+Serif:ital@0,400;1,400&family=Open+Sans:wght@400;600;700&display=swap" rel="stylesheet">
<style>
:root{
  --header-bg:#0e0e0e;
  --header-bg-2:#262626;
  --page-bg:#eeeeee;
  --panel:#f7f7f7;
  --white:#ffffff;
  --text:#333333;
  --muted:#777777;
  --faint:#aaaaaa;
  --rule:#d6d6d6;
  --divider:#9a9a9a;
  --footer-bg:#111111;
  --footer-text:#dddddd;
  --accent:#4aa3df;
  --btn:#2a2a2a;
  --ad:#8a8a8a;
}
*{box-sizing:border-box;margin:0;padding:0}
html,body{width:882px;height:1200px;overflow:hidden}
body{position:relative;background:var(--page-bg);font-family:"Open Sans",sans-serif;color:var(--text)}
.abs{position:absolute}
ul{list-style:none}

.site-header{position:absolute;left:0;top:0;width:882px;height:122px;background:linear-gradient(var(--header-bg-2),var(--header-bg))}
.brand{position:absolute;left:0;width:882px;top:36px;text-align:center;font-family:"Cabin",sans-serif;font-weight:700;font-size:34px;line-height:34px;color:var(--white)}
.social{position:absolute;top:15px;left:595px;display:flex;gap:7px}
.social span{width:23px;height:23px;border-radius:50%;background:#e9e9e9;border:2px solid #555}

.main-nav{position:absolute;left:0;top:122px;width:882px;height:36px;background:var(--white);border-bottom:1px solid var(--rule)}
.main-nav ul{position:absolute;left:131px;top:10px;width:464px;display:flex;justify-content:space-between;white-space:nowrap;font-size:9.6px;color:#222}
.search{position:absolute;left:624px;top:6px;width:111px;height:19px;border:1px solid var(--rule);border-radius:2px;font-family:"Noto Serif",serif;font-style:italic;font-size:9px;color:var(--faint);padding:3px 6px;background:var(--white)}
.search svg{position:absolute;right:4px;top:3px}

.content-divider{position:absolute;left:528px;top:158px;width:1px;height:814px;background:var(--divider)}

.breadcrumb{left:134px;top:174px;font-family:"Noto Serif",serif;font-style:italic;font-size:9px;color:var(--faint)}
.breadcrumb b{font-weight:400;color:#555}
.post-title{left:134px;top:211px;font-family:"Cabin",sans-serif;font-weight:600;font-size:16px;color:#222}
.post-meta{left:134px;top:231px;font-family:"Noto Serif",serif;font-style:italic;font-size:8px;color:var(--faint)}
.post-meta b{font-weight:400;color:#666}
.post-figure{left:134px;top:246px;width:380px;height:222px;border:5px solid #9c9c9c;border-radius:3px;background:linear-gradient(180deg,#ffffff 0%,#f2f3fb 45%,#e6e6f6 75%,#f6e6e6 100%)}
.post-body{left:136px;top:472px;width:380px;font-size:7.4px;line-height:13.4px;color:#666}

.comments-title{left:136px;top:594px;font-family:"Cabin",sans-serif;font-weight:600;font-size:15px;color:#222}
.comment{left:134px;top:624px;width:356px;height:126px;background:var(--panel);border:1px solid #e2e2e2}
.avatar{position:absolute;left:14px;top:12px;width:36px;height:36px;background:linear-gradient(#cfd4da,#9aa3ad);border:2px solid #fff;box-shadow:0 0 0 1px #bbb}
.comment h3{position:absolute;left:60px;top:8px;font-family:"Cabin",sans-serif;font-weight:600;font-size:12px;color:#222}
.comment time{position:absolute;left:60px;top:25px;font-family:"Noto Serif",serif;font-style:italic;font-size:8px;color:var(--faint)}
.comment p{position:absolute;left:60px;top:37px;width:290px;font-size:7.1px;line-height:12.2px;color:#666}
.comment-tail{left:452px;top:749px}
.btn{position:absolute;border-radius:11px;background:linear-gradient(#555,var(--btn) 55%,#111);color:#fff;font-family:"Noto Serif",serif;font-size:10px;text-align:center;box-shadow:0 1px 2px rgba(0,0,0,.4)}

.reply-title{left:136px;top:766px;font-family:"Cabin",sans-serif;font-weight:600;font-size:15px;color:#222}
.field{position:absolute;left:136px;background:var(--panel);border:1px solid #e0e0e0;font-size:7.6px;color:#777;padding:5px 14px}

.newsletter{left:540px;top:172px;width:190px;height:168px;background:var(--white);border:1px solid #e0e0e0}
.newsletter h4{position:absolute;left:14px;top:9px;font-family:"Noto Serif",serif;font-weight:400;font-size:10px;color:#333}
.newsletter .rule{position:absolute;left:0;right:0;height:1px;background:#e6e6e6}
.newsletter p{position:absolute;left:14px;top:38px;width:168px;font-size:8.4px;line-height:13px;color:#555}
.newsletter .email{position:absolute;left:14px;top:78px;width:164px;height:24px;border:1px solid #ddd;background:#f7f7f7;font-size:7.5px;color:#aaa;padding:6px 8px}
.newsletter small{position:absolute;left:10px;top:151px;font-family:"Noto Serif",serif;font-style:italic;font-size:6.6px;color:#555}

.widget-title{position:absolute;left:545px;font-size:7.8px;font-weight:400;color:var(--faint);text-transform:uppercase}
.widget-list{position:absolute;left:548px;font-size:7.6px;line-height:17.1px;color:#333}
.widget-list li::before{content:"";display:inline-block;width:3px;height:3px;background:#999;margin-right:9px;vertical-align:middle}
.widget-list li.dim{color:#aaa}
.ad{left:540px;top:728px;width:188px;height:124px;background:var(--ad);border:1px solid #777;color:#fff;font-size:12px;display:flex;align-items:center;justify-content:center}

.site-footer{position:absolute;left:0;top:972px;width:882px;height:228px;background:linear-gradient(#1c1c1c,var(--footer-bg))}
.footer-col{position:absolute;top:32px;color:var(--footer-text)}
.footer-col h5{font-size:8px;font-weight:600;color:#fff;margin-bottom:8px}
.footer-col li{font-size:7.6px;line-height:16.3px}
.footer-col.bullets li::before{content:"";display:inline-block;width:3px;height:3px;background:#777;margin:0 9px 0 -12px;vertical-align:middle}
.footer-bar{position:absolute;left:0;top:186px;width:882px;height:42px;background:#0a0a0a;border-top:1px solid #222}
.footer-bar ul{position:absolute;left:126px;top:16px;display:flex;gap:12px;font-size:7.8px;font-weight:700;color:#fff}
.footer-bar li.active{color:var(--accent);font-style:italic}
</style>
</head>
<body>

<header class="site-header">
  <div class="brand">Stock Market</div>
  <div class="social" aria-label="Social links"><span></span><span></span><span></span><span></span><span></span></div>
</header>

<nav class="main-nav">
  <ul>
    <li>Home</li><li>About</li><li>Categories</li><li>Blog</li><li>Contact Us</li><li>Some Category</li><li>Stock Techniques</li><li>Other Stuff</li>
  </ul>
  <div class="search">Search this site...
    <svg width="11" height="11" viewBox="0 0 11 11"><circle cx="6" cy="4.5" r="3.3" fill="none" stroke="#999" stroke-width="1.2"/><line x1="3.6" y1="7" x2="1" y2="10" stroke="#999" stroke-width="1.4"/></svg>
  </div>
</nav>

<div class="content-divider"></div>

<main>
  <div class="abs breadcrumb">Home &gt; Some Category &gt; <b>Post Titles Goes Here</b></div>
  <h1 class="abs post-title">Post Title Goes Here</h1>
  <div class="abs post-meta">Reviewed by <b>Admin</b> on March 13, 2013</div>
  <div class="abs post-figure" role="img" aria-label="Daily stock price chart with candlestick bars, moving average line and momentum histogram"></div>
  <p class="abs post-body">Pellentesque tempor dui non mauris ullamcorper sit amet mattis metus dapibus. Vestibulum ante ipsum primis in faucibus orci luctus et ultrices posuere cubilia Curae; Nullam tristique faucibus gravida. Donec vitae placerat nunc. Nunc ornare odio at augue viverra non fermentum quam imperdiet. Donec molestie commodo faucibus. Mauris varius, nisl sit amet sollicitudin varius, sem felis congue nulla, at malesuada leo elit nec lacus. Donec eu diam vehicula neque fermentum lacinia. Mauris vel diam dui. Integer ornare pharetra euismod. Aenean feugiat posuere augue eu hendrerit. Pellentesque tempor dui non mauris ullamcorper sit amet mattis metus dapibus. Vestibulum ante ipsum primis in faucibus orci luctus et ultrices posuere cubilia Curae; Nullam tristique faucibus gravida. Donec vitae placerat nunc. Nunc ornare</p>

  <h2 class="abs comments-title">30 Comments</h2>
  <article class="abs comment">
    <div class="avatar"></div>
    <h3>Anonymous Name</h3>
    <time>March 13, 2013</time>
    <p>Pellentesque tempor dui non mauris ullamcorper sit amet mattis metus dapibus. Vestibulum ante ipsum primis in faucibus orci luctus et ultrices posuere cubilia Curae; Nullam tristique faucibus gravida. Donec vitae placerat nunc. Nunc ornare odio at augue viverra non fermentum quam imperdiet. Donec molestie</p>
    <div class="btn" style="left:281px;top:100px;width:57px;height:20px;line-height:20px">Reply</div>
  </article>
  <svg class="abs comment-tail" width="18" height="16" viewBox="0 0 18 16"><path d="M0 0 H18 V16 Z" fill="#f7f7f7" stroke="#e2e2e2"/></svg>

  <h2 class="abs reply-title">Submit a Reply</h2>
  <div class="field" style="top:793px;width:199px;height:21px">Name</div>
  <div class="field" style="top:820px;width:199px;height:21px">Email Address</div>
  <div class="field" style="top:846px;width:303px;height:71px">Name</div>
  <div class="btn" style="left:419px;top:936px;width:66px;height:22px;line-height:22px">Reply</div>
</main>

<aside>
  <section class="abs newsletter">
    <h4>Subscribe to this newsletter</h4>
    <svg style="position:absolute;left:164px;top:12px" width="14" height="10" viewBox="0 0 14 10"><rect width="14" height="10" fill="#444"/><path d="M0 0 L7 5.5 L14 0" fill="none" stroke="#fff" stroke-width="1"/></svg>
    <div class="rule" style="top:31px"></div>
    <p>Sign up to receive email updates and to hear what's going on with us!</p>
    <div class="email">Enter E-Mail Address</div>
    <div class="btn" style="left:122px;top:109px;width:56px;height:24px;line-height:24px;border-radius:3px;font-family:'Open Sans',sans-serif;font-size:7.5px;font-weight:700">SIGN UP</div>
    <div class="rule" style="top:142px"></div>
    <small><b style="font-weight:700">WE HATE SPAM!</b> Really its terrible &amp; we never do it.</small>
  </section>

  <h4 class="widget-title" style="top:348px">Links</h4>
  <ul class="widget-list" style="top:364px">
    <li>Rhoncus quis varius sed velit nibh moles</li>
    <li class="dim">Mauris quis nunc eu nunc molestie</li>
    <li>Egestas et sit amet odio morbi quis nunc</li>
    <li>Lacinia velit in nibh sodales sed quis nunc</li>
    <li>Pharetra sem feugiat nibh sodales sed</li>
    <li>Vivamus ut cursus augue nibh sodales sed</li>
  </ul>

  <h4 class="widget-title" style="top:472px">Recent Posts</h4>
  <ul class="widget-list" style="top:488px">
    <li>Rhoncus quis varius sed velit nibh moles</li>
    <li class="dim">Mauris quis nunc eu nunc molestie</li>
    <li>Egestas et sit amet odio morbi quis nunc</li>
    <li>Lacinia velit in nibh sodales sed quis nunc</li>
    <li>Pharetra sem feugiat nibh sodales sed</li>
    <li>Vivamus ut cursus augue nibh sodales sed</li>
  </ul>

  <h4 class="widget-title" style="top:598px">Archives</h4>
  <ul class="widget-list" style="top:614px">
    <li>June 2013</li><li>May 2013</li><li>April 2013</li><li>March 2013</li><li>Februauary 2013</li><li>January 2013</li>
  </ul>

  <div class="abs ad">VORTELLI ADVERTISEMENT</div>
</aside>

<footer class="site-footer">
  <div class="footer-col" style="left:132px">
    <h5>ABOUT US</h5>
    <ul><li>Rhoncus quis varius sed velit nibh moles</li><li>Mauris quis nunc eu nunc molestie</li><li>Egestas et sit amet odio morbi quis nunc</li><li>Lacinia velit in nibh sodales sed quis nunc</li><li>Pharetra sem feugiat nibh sodales sed</li><li>Vivamus ut cursus augue nibh sodales sed</li></ul>
  </div>
  <div class="footer-col bullets" style="left:336px">
    <h5>CATEGORIES</h5>
    <ul style="padding-left:12px"><li>Rhoncus quis varius sed velit nibh moles</li><li>Mauris quis nunc eu nunc molestie</li><li>Egestas et sit amet odio morbi quis nunc</li><li>Lacinia velit in nibh sodales sed quis nunc</li><li>Pharetra sem feugiat nibh sodales sed</li><li>Vivamus ut cursus augue nibh sodales sed</li></ul>
  </div>
  <div class="footer-col bullets" style="left:544px">
    <h5>RECENT POSTS</h5>
    <ul style="padding-left:12px"><li>Rhoncus quis varius sed velit nibh moles</li><li>Mauris quis nunc eu nunc molestie</li><li>Egestas et sit amet odio morbi quis nunc</li><li>Lacinia velit in nibh sodales sed quis nunc</li><li>Pharetra sem feugiat nibh sodales sed</li><li>Vivamus ut cursus augue nibh sodales sed</li></ul>
  </div>
  <div class="footer-bar">
    <ul><li class="active">Home</li><li>About</li><li>Categories</li><li>Shortcodes</li><li>Page Templates</li><li>Blog</li><li>Contact Us</li></ul>
  </div>
</footer>

</body>
</html>
```